Varnell Consulting needs a business card design

Varnell Consulting is a small business that consults and trains Australia wide in Workplace Health and Safety, Environment and Quality Management Systems.

Clients are typically smaller businesses with 50 to 200 employees but there are some large clients.

Communication is often by email, although mobile is used as well.

Varnell Consulting
47 Tessock Downs Road
Marrowby, QLD 4317
0438 291 604

```html
<!DOCTYPE html>
<html lang="en">
<head>
<meta charset="utf-8">
<title>Varnell Consulting – Business Card</title>
<link rel="stylesheet" href="https://fonts.googleapis.com/css2?family=Open+Sans:wght@400;600;700&display=swap">
<style>
  :root{
    --page:#e4e4e6;
    --navy-deep:#2a2c5c;
    --blue:#2f5f9c;
    --paper:#f1f1f2;
    --edge:#c9cacd;
    --ink:#2d4f8e;
    --white:#ffffff;
    --muted:#d4d8ea;
    --icon:#9fb3dd;
  }
  *{box-sizing:border-box;margin:0;padding:0}
  html,body{width:1200px;height:961px;overflow:hidden}
  body{
    background:var(--page);
    font-family:"Open Sans",Arial,sans-serif;
    position:relative;
  }
  .card{
    position:absolute;
    width:520px;height:318px;
    border-radius:26px;
    overflow:hidden;
    box-shadow:0 10px 24px rgba(0,0,0,.16);
    background:var(--paper);
  }
  .card svg.card-bg{position:absolute;inset:0;width:100%;height:100%}
  .card--front{left:60px;top:170px}
  .card--back{left:620px;top:470px}

  .holder{position:absolute;left:46px;top:108px;color:var(--white)}
  .holder-name{font-size:23px;font-weight:700;letter-spacing:.5px;text-transform:uppercase;line-height:1.1}
  .holder-role{font-size:16px;font-weight:400;color:var(--muted);margin-top:2px;padding-left:10px}

  .contact-list{position:absolute;left:56px;top:206px;list-style:none;color:var(--white);font-size:12.5px;line-height:19px}
  .contact-list li{display:flex;align-items:center;gap:7px;white-space:nowrap}
  .contact-list li.indent{padding-left:19px}
  .contact-icon{width:12px;height:12px;flex:none}

  .brand{
    position:absolute;
    display:flex;align-items:center;gap:12px;
    color:var(--ink);font-weight:700;
  }
  .brand-dot{width:22px;height:22px;border-radius:50%;background:var(--ink);flex:none}
  .brand-name{display:flex;flex-direction:column;line-height:1}
  .brand-name .line-main{font-size:34px;letter-spacing:.5px}
  .brand-name .line-sub{font-size:15px;letter-spacing:2.4px;margin-top:5px}
  .card--front .brand{left:318px;top:122px}
  .card--back .brand{left:48px;top:132px}
  .card--front .brand-name .line-main{font-size:29px}
  .card--front .brand-name .line-sub{font-size:13px;letter-spacing:2px}
</style>
</head>
<body>

<section class="card card--front" aria-label="Card front with contact details">
  <svg class="card-bg" viewBox="0 0 520 318" preserveAspectRatio="none" aria-hidden="true">
    <defs>
      <linearGradient id="frontBlue" x1="0" y1="1" x2="1" y2="0">
        <stop offset="0" stop-color="#2a2c5c"/>
        <stop offset="1" stop-color="#2f5f9c"/>
      </linearGradient>
    </defs>
    <rect width="520" height="318" fill="#f1f1f2"/>
    <path d="M0 0 H300 C250 80 245 230 318 318 H0 Z" fill="url(#frontBlue)"/>
    <path d="M300 0 C250 80 245 230 318 318" fill="none" stroke="#c9cacd" stroke-width="5"/>
  </svg>

  <div class="holder">
    <p class="holder-name">Owen Varnell</p>
    <p class="holder-role">Manager</p>
  </div>

  <ul class="contact-list">
    <li>
      <svg class="contact-icon" viewBox="0 0 12 12" aria-hidden="true"><circle cx="6" cy="6" r="5.4" fill="none" stroke="#9fb3dd" stroke-width="1"/><path d="M4 3.3l1 .9-.5.9c.4.8 1 1.4 1.8 1.8l.9-.5.9 1-.6.9c-1.9-.3-3.6-2-3.9-3.9z" fill="#9fb3dd"/></svg>
      0438 291 604
    </li>
    <li>
      <svg class="contact-icon" viewBox="0 0 12 12" aria-hidden="true"><circle cx="6" cy="6" r="5.4" fill="none" stroke="#9fb3dd" stroke-width="1"/><rect x="3" y="4" width="6" height="4" fill="none" stroke="#9fb3dd" stroke-width=".9"/><path d="M3 4l3 2.2L9 4" fill="none" stroke="#9fb3dd" stroke-width=".9"/></svg>
      o.varnell@varnellmail.com.au
    </li>
    <li class="indent">47 Tessock Downs Road</li>
    <li class="indent">Marrowby, QLD 4317</li>
  </ul>

  <div class="brand">
    <span class="brand-dot"></span>
    <span class="brand-name"><span class="line-main">VARNELL</span><span class="line-sub">CONSULTING</span></span>
  </div>
</section>

<section class="card card--back" aria-label="Card back with company name">
  <svg class="card-bg" viewBox="0 0 520 318" preserveAspectRatio="none" aria-hidden="true">
    <defs>
      <linearGradient id="backBlue" x1="0" y1="1" x2="1" y2="0">
        <stop offset="0" stop-color="#2f5f9c"/>
        <stop offset="1" stop-color="#2a2c5c"/>
      </linearGradient>
    </defs>
    <rect width="520" height="318" fill="url(#backBlue)"/>
    <path d="M0 0 H285 C350 80 360 220 320 318 H0 Z" fill="#f1f1f2"/>
    <path d="M285 0 C350 80 360 220 320 318" fill="none" stroke="#c9cacd" stroke-width="5"/>
  </svg>

  <div class="brand">
    <span class="brand-dot"></span>
    <span class="brand-name"><span class="line-main">VARNELL</span><span class="line-sub">CONSULTING</span></span>
  </div>
</section>

</body>
</html>
```